Design a Job Application & CV

I need a design for upcoming job applications that includes a cv. It needs to look as elegant and modern as possible as the application will be send mainly to large corporations and strategy consultancies. I have attached an application that I like for your consideration. One of the more difficult requirements is that it needs to be editable in ms office word for mac/windows.
As stated only the design is part of this project. I will fill in my content later on.
Updates
Project Deadline Extended
Reason: Dear Designers,
I am going to increase the budget as well as extending the deadline. I am hoping that you can improve upon the design that I have provided in the brief. If you have questions please let me know.
Dear Designers,
Target Market(s)
Human Resources Managers, Senior Consultants and Executives of larger firms
Industry/Entity Type
Office
Requirements
Must have
- 4 Pages including( a cover page, a coverletter page, 2 pages cv)
It should be easy to edit and should be readable by word for mac, i.e. in the *.docx format.
Here is an example of what I like:
http://www.torvenmaal.de/applicationexample.pdf
http://www.torvenmaal.de/applicationExample.docx
colors that I like are blue, grey, black, white
Nice to have
- icons to indicate sections
Should not have
- invasive cliparts

```html
<!DOCTYPE html>
<html lang="en">
<head>
<meta charset="utf-8">
<title>Experiences – CV Page</title>
<link rel="stylesheet" href="https://fonts.googleapis.com/css2?family=Quicksand:wght@400;500&family=Didact+Gothic&display=swap">
<style>
  :root {
    --page-grey: #6d6e71;
    --text-light: #f1f1f1;
    --rule-dots: #f4f4f4;
    --navy-deep: #10263d;
    --navy-mid: #1d4a72;
    --blue-bright: #2f7fb8;
    --swoosh-white: #ffffff;
    --swoosh-silver: #c9ced3;
  }
  html, body {
    margin: 0;
    padding: 0;
    overflow: hidden;
    background: var(--page-grey);
  }
  .cv-page {
    position: relative;
    width: 848px;
    height: 1200px;
    overflow: hidden;
    background: var(--page-grey);
    font-family: "Didact Gothic", "Century Gothic", sans-serif;
    color: var(--text-light);
  }
  .page-header {
    position: absolute;
    left: 0;
    top: 0;
    width: 848px;
    height: 150px;
  }
  .page-title {
    position: absolute;
    left: 40px;
    top: 4px;
    margin: 0;
    font-family: "Quicksand", "Century Gothic", sans-serif;
    font-weight: 400;
    font-size: 54px;
    letter-spacing: 0.5px;
    color: #ffffff;
  }
  .entry {
    position: absolute;
    left: 42px;
    width: 764px;
  }
  .entry-period {
    margin: 0;
    font-size: 17px;
    line-height: 22px;
  }
  .entry-org {
    margin: 6px 0 0;
    padding-top: 8px;
    border-top: 2.5px dotted var(--rule-dots);
    font-size: 17.5px;
    line-height: 24px;
    text-transform: uppercase;
    letter-spacing: 0.2px;
  }
  .entry-text {
    margin: 6px 0 0;
    font-size: 17.5px;
    line-height: 38.6px;
  }
  .entry--halden { top: 176px; }
  .entry--brennock { top: 488px; }
  .entry--lisvane { top: 758px; }
  .entry--kilbrook { top: 982px; }
</style>
</head>
<body>
<main class="cv-page">
  <header class="page-header">
    <svg width="848" height="150" viewBox="0 0 848 150" aria-hidden="true">
      <defs>
        <linearGradient id="bandGradient" x1="0" y1="0" x2="1" y2="0">
          <stop offset="0" stop-color="var(--navy-deep)"/>
          <stop offset="0.55" stop-color="var(--navy-mid)"/>
          <stop offset="1" stop-color="var(--blue-bright)"/>
        </linearGradient>
        <linearGradient id="bandShade" x1="0" y1="0" x2="0" y2="1">
          <stop offset="0" stop-color="#000" stop-opacity="0.35"/>
          <stop offset="1" stop-color="#000" stop-opacity="0"/>
        </linearGradient>
      </defs>
      <path class="swoosh-white" d="M0 72 C260 96 560 112 848 86 V126 C600 112 300 112 0 118 Z" fill="var(--swoosh-white)"/>
      <path class="swoosh-silver" d="M0 112 C300 104 600 104 848 120 V128 C600 114 300 114 0 122 Z" fill="var(--swoosh-silver)"/>
      <path class="header-band" d="M0 0 H848 V86 C600 108 300 96 0 72 Z" fill="url(#bandGradient)"/>
      <path class="header-band-shade" d="M0 0 H848 V86 C600 108 300 96 0 72 Z" fill="url(#bandShade)"/>
    </svg>
    <h1 class="page-title">Experiences</h1>
  </header>

  <section class="entry entry--halden">
    <p class="entry-period">2003 – 2004</p>
    <h2 class="entry-org">Halden Construction Contractors, Melbourne, Australia</h2>
    <p class="entry-text">Assistant Engineer Secured work experience as an Assistant Engineer reporting directly to the Project Manager.&nbsp; Liased with Engineers and reported to Project Manager on all tasks. Conducted demolition work which included working with dangerous chemicals such as asbestos. Completed survey work using laser instruments. Ensured health &amp; safety procedures were adhered to and reported any breaches.</p>
  </section>

  <section class="entry entry--brennock">
    <p class="entry-period">2002 - 2003</p>
    <h2 class="entry-org">Brennock Electronic Design Services, Cork</h2>
    <p class="entry-text">Trainee Engineer Reported to the Senior Engineer. Assisted with designing and building of web pages. Liaised with Engineering staff on all aspects of web content relevant to the industry sector. Trained on Pagewright Editor for web design. Reported on progress at weekly team meetings.</p>
  </section>

  <section class="entry entry--lisvane">
    <p class="entry-period">1999 - 2002</p>
    <h2 class="entry-org">Lisvane University College</h2>
    <p class="entry-text">Information Assistant, Riverside Arena Checked membership cards at the information desk. Provided assistance and information to customers. Collected money for aerobics and yoga classes.&nbsp; Managed special group bookings of facilities.</p>
  </section>

  <section class="entry entry--kilbrook">
    <p class="entry-period">1993 - 1999</p>
    <h2 class="entry-org">Kilbrook Brothers College, Quayside, Cork</h2>
    <p class="entry-text">Leaving Certificate: 500 Points including an A1 in Physics.</p>
  </section>
</main>
</body>
</html>
```